Veltrano Professional Services Website

Small website for company presence and information. Company is an IT/Telecom services company. We provide presales and installation services. Included are various company logos including color levels. Site doesn't have to use these exact colors in the logos, but should be complimentary if using different colors. It should have a professional business appearance.
Updates

My apologies for not being more responsive on the designs that have been submitted. I will be narrowing down the submissions and providing additional feedback next week. Thank you for your patience.

Project Deadline Extended
Reason: Sorry again for delays on picking designs. Work has me very busy and I've just not had the time to devote to this project. I am extending the design deadline for a few more days to give me time to make my final decisions. Thank you all for your patience. Stay tuned....

Target Market(s)

Telecom sales companies that sell Brintel telecom products.

Industry/Entity Type

Professional Service

Coding

Coded - Design and coding required

Number of Pages Required

5+ page

Font styles to use
Sans Serif

Colors
3276b5
0355a3
85abd2
85cae6
33a6d7
0692cd
ffffff

Requirements
Must have
• Professional design reflective of IT/Telecom business. A good reference website would be: http://www.quollanetworks.example/. Looking for something similar in function and presence.
Nice to have
• Rolling photos highlighting our services. Traditional navigation across the top of all pages.
Should not have
• No motion video, flashy presentation or overly confused interface.

```html
<!DOCTYPE html>
<html lang="en">
<head>
<meta charset="utf-8">
<title>Veltrano Professional Services</title>
<link rel="stylesheet" href="https://fonts.googleapis.com/css2?family=Open+Sans:wght@400;600;700&family=Roboto+Condensed:wght@700&display=swap">
<style>
:root{
  --brand:#0355a3;
  --brand-mid:#3276b5;
  --brand-dark:#033f80;
  --light-blue:#85abd2;
  --ink:#222;
  --body:#555;
  --muted:#9a9a9a;
  --panel:#f3f3f3;
  --card:#ededed;
  --badge:#2b2b2b;
  --footer:#26262c;
  --white:#fff;
}
*{margin:0;padding:0;box-sizing:border-box}
html,body{width:1200px;height:2719px;overflow:hidden}
body{position:relative;background:var(--white);font-family:"Open Sans",Arial,sans-serif;color:var(--body)}
.abs{position:absolute}
h2.section-title{font-family:"Roboto Condensed",Arial,sans-serif;font-weight:700;font-size:27px;color:var(--ink);text-align:center;letter-spacing:.2px}

/* header */
.site-header{left:0;top:0;width:1200px;height:88px}
.brand{left:80px;top:21px;display:flex;align-items:center;gap:10px;color:var(--brand);font-weight:700}
.brand-mark{width:40px;height:40px;background:var(--brand)}
.brand-name{font-size:29px;line-height:30px;letter-spacing:1px}
.brand-sub{font-size:9px;line-height:12px;letter-spacing:.8px}
.main-nav{right:136px;top:34px;display:flex;gap:27px}
.main-nav a{font-size:13px;font-weight:700;color:var(--brand);text-decoration:none}

/* hero */
.hero{left:7px;top:88px;width:1186px;height:472px;background:linear-gradient(120deg,#6d6a66 0%,#a9a49c 35%,#cfc9bf 60%,#8a8680 100%)}
.hero-arrow{top:220px;width:24px;height:30px}
.hero-caption{left:704px;top:300px;width:340px;padding:8px 14px 14px;background:rgba(40,40,45,.55);color:var(--white)}
.hero-caption h1{font-weight:400;font-size:50px;line-height:58px}
.hero-caption p{font-size:11px;line-height:15px;margin-top:4px}

/* call to action band */
.cta-band{left:0;top:560px;width:1200px;height:122px;background:var(--brand-dark)}
.cta-band h3{position:absolute;left:78px;top:34px;font-size:20px;font-weight:700;color:var(--white)}
.cta-band p{position:absolute;left:78px;top:70px;font-size:12px;color:var(--white)}
.btn-outline-light{position:absolute;left:938px;top:43px;width:174px;height:40px;border:2px solid var(--white);color:var(--white);font-size:11px;font-weight:700;letter-spacing:1px;display:flex;align-items:center;justify-content:center}

/* about */
.about{left:0;top:752px;width:1200px}
.about p{width:870px;margin:24px auto 0;text-align:center;font-size:11px;line-height:21.8px;color:var(--body)}
.btn-solid{display:flex;align-items:center;justify-content:center;width:104px;height:40px;margin:26px auto 0;background:var(--brand);color:var(--white);font-size:10px;font-weight:700;letter-spacing:.5px}

/* services */
.services{left:0;top:1138px;width:1200px;height:820px;background:var(--panel)}
.services .section-title{margin-top:70px}
.services .lead{text-align:center;font-size:12px;margin-top:14px}
.service-card{top:157px;width:240px;height:305px;background:var(--card);border:2px solid var(--light-blue);text-align:center}
.service-icon{display:block;margin:40px auto 0}
.service-card h4{font-size:17px;font-weight:700;color:var(--ink);margin-top:20px}
.service-card p{font-size:12px;line-height:22px;margin:18px auto 0;width:190px}
.pill-grey{display:inline-flex;align-items:center;gap:6px;margin-top:18px;height:28px;padding:0 18px;border-radius:14px;background:#a9a9a9;color:var(--white);font-size:8px;font-weight:700;letter-spacing:.8px}
.pill-grey svg{display:block}
.contact-box{top:560px;width:507px;height:205px;border:2px solid var(--light-blue);text-align:center}
.contact-box h4{display:flex;align-items:center;justify-content:center;gap:8px;margin-top:32px;font-size:16px;font-weight:700;color:var(--brand-mid)}
.contact-box p{font-size:12px;line-height:22px;margin-top:28px}
.contact-box b{color:var(--brand);font-weight:700}
.pill-outline{position:absolute;left:50%;bottom:-16px;transform:translateX(-50%);width:118px;height:32px;border-radius:16px;border:2px solid var(--brand-mid);background:var(--white);color:var(--brand);font-size:10px;font-weight:700;letter-spacing:.8px;display:flex;align-items:center;justify-content:center}

/* process */
.process-title{left:0;top:2010px;width:664px}
.process-list{left:98px;top:2058px;width:490px;list-style:none}
.process-list li{position:relative;padding-left:28px;margin-bottom:14px}
.process-list li svg{position:absolute;left:0;top:1px}
.process-list h5{font-size:12.5px;font-weight:700;color:var(--ink)}
.process-list p{font-size:11.5px;line-height:22px;margin-top:2px;color:#777}
.process-photo{left:613px;top:2046px;width:508px;height:336px;background:linear-gradient(160deg,#d8dde2 0%,#eef0f2 45%,#b9c0c6 100%)}

/* partners */
.partners-title{left:0;top:2414px;width:1200px}
.partner-badge{background:var(--badge)}

/* footer */
.site-footer{left:0;top:2664px;width:1200px;height:55px;background:var(--footer)}
.site-footer p{position:absolute;left:78px;top:22px;font-size:10px;color:#8a8a8a}
</style>
</head>
<body>

<header class="site-header abs">
  <div class="brand abs">
    <span class="brand-mark"></span>
    <div>
      <div class="brand-name">VELTRANO</div>
      <div class="brand-sub">PROFESSIONAL SERVICES</div>
    </div>
  </div>
  <nav class="main-nav abs">
    <a href="#">HOME</a><a href="#">ABOUT US</a><a href="#">OUR SERVICES</a><a href="#">OUR PARTNERS</a><a href="#">CONTACT US</a>
  </nav>
</header>

<section class="hero abs" role="img" aria-label="Photo of a business team meeting around a table in a bright office">
  <svg class="hero-arrow abs" style="left:8px" viewBox="0 0 24 30"><path d="M17 3 5 15l12 12" fill="none" stroke="#fff" stroke-width="3"/></svg>
  <svg class="hero-arrow abs" style="right:8px" viewBox="0 0 24 30"><path d="M7 3l12 12L7 27" fill="none" stroke="#fff" stroke-width="3"/></svg>
  <div class="hero-caption abs">
    <h1>Lorem Ipsum</h1>
    <p>Lorem ipsum dolor sit amet, consetetur sadipscing elitr sed diam nonumy eirmod tempor invidunt ut labore et dolore magna aliquyam erat sed diam voluptua.</p>
  </div>
</section>

<section class="cta-band abs">
  <h3>Let's Get Started With Your Project Today!</h3>
  <p>We are Trusted. We are Reliable. We are Dependable. We are Simple.</p>
  <span class="btn-outline-light">ENJOY OUR SERVICES</span>
</section>

<section class="about abs">
  <h2 class="section-title">ABOUT VELTRANO</h2>
  <p>Lorem ipsum dolor sit amet, consetetur sadipscing elitr, sed diam nonumy eirmod tempor invidunt ut labore et dolore magna aliquyam erat, sed diam voluptua. At vero eos et accusam et justo duo dolores et ea rebum. Stet clita kasd gubergren, no sea takimata sanctus est Lorem ipsum dolor sit amet. Lorem ipsum dolor sit amet, consetetur sadipscing elitr, sed diam nonumy eirmod tempor invidunt ut labore et dolore magna aliquyam erat, sed diam voluptua. At vero eos et accusam et justo duo dolores et ea rebum. Stet clita kasd gubergren, no sea takimata sanctus est Lorem ipsum dolor sit amet. Lorem ipsum dolor sit amet, consetetur sadipscing elitr, sed diam nonumy eirmod tempor invidunt ut labore et dolore magna aliquyam erat, sed diam voluptua At vero eos et accusam et justo duo dolores et ea rebum. Stet clita kasd gubergren, no sea takimata sanctus est Lorem ipsum dolor sit amet. Stet clita kasd gubergren, no sea takimata sanctus est Lorem ipsum dolor sit amet. Stet clita kasd gubergren, no sea takimata sanctus est Lorem ipsum dolor sit amet. Stet clita kasd gubergren, no sea takimata sanctus est Lorem ipsum dolor sit amet. Stet clita kasd gubergren, no sea takimata sanctus est Lorem ipsum dolor sit amet. Stet clita kasd gubergren, no sea takimata sanctus est Lorem ipsum dolor sit amet. Stet clita kasd gubergren.</p>
  <span class="btn-solid">READ MORE</span>
</section>

<section class="services abs">
  <h2 class="section-title">OUR PROFESSIONAL SERVICES</h2>
  <p class="lead">Lorem ipsum dolor sit amet consetetur sadipscing elitr sed diam.</p>

  <div class="service-card abs" style="left:80px">
    <svg class="service-icon" width="70" height="40" viewBox="0 0 70 40"><path d="M14 34h30a10 10 0 0 0 0-20 13 13 0 0 0-25-2 11 11 0 0 0-5 22z" fill="none" stroke="#3276b5" stroke-width="3"/><path d="M54 14a10 10 0 0 1 0 14M60 9a17 17 0 0 1 0 24" fill="none" stroke="#3276b5" stroke-width="3"/></svg>
    <h4>Lorem Ipsum</h4>
    <p>Lorem ipsum dolor sit amet consetetur sadipscing elitr sed diam nonumy eirmod tempor invidunt ut labore et dolore.</p>
    <span class="pill-grey">READ MORE <svg width="10" height="10" viewBox="0 0 10 10"><circle cx="5" cy="5" r="5" fill="#fff"/><path d="M4 3l2 2-2 2" stroke="#a9a9a9" fill="none" stroke-width="1.5"/></svg></span>
  </div>
  <div class="service-card abs" style="left:347px">
    <svg class="service-icon" width="70" height="40" viewBox="0 0 70 40"><path d="M14 34h30a10 10 0 0 0 0-20 13 13 0 0 0-25-2 11 11 0 0 0-5 22z" fill="none" stroke="#3276b5" stroke-width="3"/><path d="M54 14a10 10 0 0 1 0 14M60 9a17 17 0 0 1 0 24" fill="none" stroke="#3276b5" stroke-width="3"/></svg>
    <h4>Lorem Ipsum</h4>
    <p>Lorem ipsum dolor sit amet consetetur sadipscing elitr sed diam nonumy eirmod tempor invidunt ut labore et dolore.</p>
    <span class="pill-grey">READ MORE <svg width="10" height="10" viewBox="0 0 10 10"><circle cx="5" cy="5" r="5" fill="#fff"/><path d="M4 3l2 2-2 2" stroke="#a9a9a9" fill="none" stroke-width="1.5"/></svg></span>
  </div>
  <div class="service-card abs" style="left:614px">
    <svg class="service-icon" width="70" height="40" viewBox="0 0 70 40"><path d="M14 34h30a10 10 0 0 0 0-20 13 13 0 0 0-25-2 11 11 0 0 0-5 22z" fill="none" stroke="#3276b5" stroke-width="3"/><path d="M54 14a10 10 0 0 1 0 14M60 9a17 17 0 0 1 0 24" fill="none" stroke="#3276b5" stroke-width="3"/></svg>
    <h4>Lorem Ipsum</h4>
    <p>Lorem ipsum dolor sit amet consetetur sadipscing elitr sed diam nonumy eirmod tempor invidunt ut labore et dolore.</p>
    <span class="pill-grey">READ MORE <svg width="10" height="10" viewBox="0 0 10 10"><circle cx="5" cy="5" r="5" fill="#fff"/><path d="M4 3l2 2-2 2" stroke="#a9a9a9" fill="none" stroke-width="1.5"/></svg></span>
  </div>
  <div class="service-card abs" style="left:881px">
    <svg class="service-icon" width="70" height="40" viewBox="0 0 70 40"><path d="M14 34h30a10 10 0 0 0 0-20 13 13 0 0 0-25-2 11 11 0 0 0-5 22z" fill="none" stroke="#3276b5" stroke-width="3"/><path d="M54 14a10 10 0 0 1 0 14M60 9a17 17 0 0 1 0 24" fill="none" stroke="#3276b5" stroke-width="3"/></svg>
    <h4>Lorem Ipsum</h4>
    <p>Lorem ipsum dolor sit amet consetetur sadipscing elitr sed diam nonumy eirmod tempor invidunt ut labore et dolore.</p>
    <span class="pill-grey">READ MORE <svg width="10" height="10" viewBox="0 0 10 10"><circle cx="5" cy="5" r="5" fill="#fff"/><path d="M4 3l2 2-2 2" stroke="#a9a9a9" fill="none" stroke-width="1.5"/></svg></span>
  </div>

  <div class="contact-box abs" style="left:80px">
    <h4><svg width="34" height="34" viewBox="0 0 34 34"><path d="M8 4l6 6-3 4c2 4 5 7 9 9l4-3 6 6-4 4C15 30 4 19 4 8z" fill="none" stroke="#3276b5" stroke-width="2.2" stroke-linejoin="round"/><path d="M20 4a10 10 0 0 1 10 10M20 9a5 5 0 0 1 5 5" fill="none" stroke="#3276b5" stroke-width="2.2"/></svg>Call Us Now</h4>
    <p>Need help with your services? No problem!<br>Our support technicians are here to help you<br>Phone Number: <b>123-456-7890</b>, <b>123-456-7890</b></p>
    <span class="pill-outline">LET'S TALK</span>
  </div>
  <div class="contact-box abs" style="left:614px">
    <h4><svg width="34" height="30" viewBox="0 0 34 30"><path d="M3 4h18v12H9l-5 4v-4H3z" fill="#0355a3"/><path d="M23 9h8v12h-2v4l-5-4H12v-3h11z" fill="#0355a3"/></svg>Email Us</h4>
    <p>Welcome to Veltrano Customer Service! Please feel free to ask<br>any questions you have. We would love to hear from you.<br>Email Address: <b>supports@veltrano.example</b></p>
    <span class="pill-outline">GET STARTED</span>
  </div>
</section>

<h2 class="section-title process-title abs">HOW WE DO IT</h2>
<ul class="process-list abs">
  <li><svg width="16" height="16" viewBox="0 0 16 16"><circle cx="8" cy="8" r="8" fill="#0355a3"/><path d="M4.5 8.2l2.3 2.3 4.7-4.7" stroke="#fff" stroke-width="2" fill="none"/></svg><h5>Lorem Ipsum Dolor Sit Amet</h5><p>Lorem ipsum dolor sit amet, consetetur sadipscing elitr sed diam nonumy eirmod tempor invidunt ut labore et dolore magna aliquyam erat sed diam voluptua.</p></li>
  <li><svg width="16" height="16" viewBox="0 0 16 16"><circle cx="8" cy="8" r="8" fill="#0355a3"/><path d="M4.5 8.2l2.3 2.3 4.7-4.7" stroke="#fff" stroke-width="2" fill="none"/></svg><h5>Lorem Ipsum Dolor Sit Amet</h5><p>Lorem ipsum dolor sit amet, consetetur sadipscing elitr sed diam nonumy eirmod tempor invidunt ut labore et dolore magna aliquyam erat sed diam voluptua.</p></li>
  <li><svg width="16" height="16" viewBox="0 0 16 16"><circle cx="8" cy="8" r="8" fill="#0355a3"/><path d="M4.5 8.2l2.3 2.3 4.7-4.7" stroke="#fff" stroke-width="2" fill="none"/></svg><h5>Lorem Ipsum Dolor Sit Amet</h5><p>Lorem ipsum dolor sit amet, consetetur sadipscing elitr sed diam nonumy eirmod tempor invidunt ut labore et dolore magna aliquyam erat sed diam voluptua.</p></li>
  <li><svg width="16" height="16" viewBox="0 0 16 16"><circle cx="8" cy="8" r="8" fill="#0355a3"/><path d="M4.5 8.2l2.3 2.3 4.7-4.7" stroke="#fff" stroke-width="2" fill="none"/></svg><h5>Lorem Ipsum Dolor Sit Amet</h5><p>Lorem ipsum dolor sit amet, consetetur sadipscing elitr sed diam nonumy eirmod tempor invidunt ut labore et dolore magna aliquyam erat sed diam voluptua.</p></li>
</ul>
<div class="process-photo abs" role="img" aria-label="Photo of a support desk with several computer monitors and a desk microphone"></div>

<h2 class="section-title partners-title abs">OUR PARTNERS</h2>
<div class="partner-badge abs" style="left:142px;top:2506px;width:104px;height:66px;border-radius:33px"></div>
<div class="partner-badge abs" style="left:346px;top:2498px;width:94px;height:86px;border-radius:50%"></div>
<div class="partner-badge abs" style="left:544px;top:2514px;width:108px;height:54px"></div>
<div class="partner-badge abs" style="left:754px;top:2492px;width:94px;height:98px;border-radius:10px"></div>
<div class="partner-badge abs" style="left:952px;top:2506px;width:108px;height:66px;border-radius:33px"></div>

<footer class="site-footer abs">
  <p>© Veltrano, 2017. All Rights Reserved.</p>
</footer>

</body>
</html>
```